Personal letterhead and stationary

I am looking for someone to design letterhead and stationary set for my personal use. I want something simple and timeless with a little bit of color. I like photography, computers and writing.

```html
<!DOCTYPE html>
<html lang="en">
<head>
<meta charset="utf-8">
<title>Theodore Jay Carson — Letterhead</title>
<link rel="stylesheet" href="https://fonts.googleapis.com/css2?family=Josefin+Sans:wght@300;400;700&display=swap">
<style>
  :root {
    --leaf: #8dab5c;
    --paper: #ffffff;
    --sheet: #fdfdfb;
    --ink: #111111;
    --sheet-edge: #c9c9c9;
  }
  * { margin: 0; padding: 0; box-sizing: border-box; }
  html, body { width: 1200px; height: 1000px; overflow: hidden; background: var(--paper); }
  body { position: relative; font-family: "Josefin Sans", "Century Gothic", sans-serif; color: var(--ink); }

  /* Masthead band */
  .masthead { position: absolute; left: 0; top: 0; width: 1200px; height: 277px; background: var(--leaf); overflow: hidden; }
  .rule { position: absolute; background: var(--paper); }
  .rule--left-drop  { left: 46px;  top: 0;     width: 7px;   height: 229px; }
  .rule--left-run   { left: 46px;  top: 222px; width: 380px; height: 7px; }
  .rule--right-run  { left: 1130px; top: 220px; width: 44px; height: 7px; }
  .rule--right-drop { left: 1167px; top: 220px; width: 7px;  height: 57px; }

  .nameplate {
    position: absolute; left: 89px; top: 41px; width: 1023px; height: 134px;
    background: var(--paper);
    display: flex; align-items: center; justify-content: center;
    font-size: 56px; letter-spacing: 0.3em; line-height: 1; padding-top: 8px;
    white-space: nowrap; overflow: hidden;
  }
  .nameplate .given, .nameplate .family { font-weight: 700; }
  .nameplate .middle { font-weight: 300; margin: 0 0.2em; }
  .nameplate .family { margin-right: -0.3em; }

  .address {
    position: absolute; left: 418px; top: 207px; width: 720px; height: 37px;
    background: var(--paper);
    display: flex; align-items: center; justify-content: center;
    font-size: 15px; font-weight: 400; letter-spacing: 0.36em; padding-top: 3px;
    white-space: nowrap; overflow: hidden;
  }

  /* Letterhead sheet preview */
  .sheet {
    position: absolute; left: 617px; top: 493px; width: 468px; height: 560px;
    background: var(--sheet); border: 1px solid var(--sheet-edge); overflow: hidden;
  }
  .sheet .masthead { transform: scale(0.39); transform-origin: 0 0; left: -1px; top: -1px; }
</style>
</head>
<body>
  <header class="masthead">
    <span class="rule rule--left-drop"></span>
    <span class="rule rule--left-run"></span>
    <span class="rule rule--right-run"></span>
    <span class="rule rule--right-drop"></span>
    <h1 class="nameplate"><span class="given">THEODORE</span><span class="middle">JAY</span><span class="family">CARSON</span></h1>
    <p class="address">2750 CAMERA RIDGE ROAD, SAN MATEO, CA 94402</p>
  </header>

  <section class="sheet" aria-label="Letterhead page">
    <div class="masthead">
      <span class="rule rule--left-drop"></span>
      <span class="rule rule--left-run"></span>
      <span class="rule rule--right-run"></span>
      <span class="rule rule--right-drop"></span>
      <p class="nameplate"><span class="given">THEODORE</span><span class="middle">JAY</span><span class="family">CARSON</span></p>
      <p class="address">2750 CAMERA RIDGE ROAD, SAN MATEO, CA 94402</p>
    </div>
  </section>
</body>
</html>
```